Digital Price Menus for Detail Shop

I am looking to have digital menus for my detail shop. I have 3 55-inch TVs (see pictures) on how they are situated on the wall for my front desk area. They will be vertical, not horizontal.

Color pallet I am looking for is black and gold, with some accent colors if applicable. I would like black background with some sort of design in it in such a way it looks faint or ghosted in the background ... i.e., honeycomb, splatter, etc. A boarder is optional.

Needs to be designed well, organized well and easy to read for customers walking in.

the each document is for each TV, Interior, Exterior and Ceramic Coatings

Company logo files included. would like my logos on them as well

Target Market(s)

Customers walking in to my shop, easy to read and understand

Industry/Entity Type

Car wash, Detailing

Colors

Designer to choose only greyscale colors for use in the design.

Requirements
Nice to have
• Professional Look
Should not have
• tacky look

```html
<!DOCTYPE html>
<html lang="en">
<head>
<meta charset="utf-8">
<title>Interior Detail Packages</title>
<link rel="stylesheet" href="https://fonts.googleapis.com/css2?family=Bebas+Neue&family=Montserrat:wght@500&display=swap">
<style>
  :root{
    --ink:#000000;
    --panel:#090909;
    --paper:#ffffff;
    --text:#f2f2f2;
    --gold-dark:#9c6a1e;
    --gold-mid:#c99d34;
    --gold-light:#d9b53c;
    --rule:#b48a2a;
    --texture-a:rgba(44,44,44,.55);
    --texture-b:rgba(26,26,26,.35);
  }
  *{margin:0;padding:0;box-sizing:border-box}
  html,body{width:676px;height:1200px;overflow:hidden;background:var(--paper)}
  .menu{position:relative;width:676px;height:1200px;background:var(--paper);font-family:"Montserrat",sans-serif}
  .board{position:absolute;left:26px;top:52px;width:622px;height:1104px;background:var(--panel)}
  .board-texture{position:absolute;left:26px;top:123px;width:622px;height:1014px;
    background:
      radial-gradient(ellipse 60% 35% at 30% 35%,var(--texture-a),transparent 70%),
      radial-gradient(ellipse 55% 30% at 70% 62%,var(--texture-a),transparent 70%),
      radial-gradient(ellipse 50% 25% at 35% 85%,var(--texture-b),transparent 70%),
      linear-gradient(180deg,rgba(18,18,18,.4),rgba(10,10,10,.1))}
  .header-band{position:absolute;left:26px;top:52px;width:622px;height:71px;
    background:linear-gradient(90deg,var(--gold-dark),var(--gold-light) 50%,var(--gold-dark));
    display:flex;align-items:center;justify-content:center}
  .header-band h1{font-family:"Bebas Neue",sans-serif;font-weight:400;font-size:54px;line-height:1;
    letter-spacing:3.6px;color:var(--ink);padding-top:6px}
  .footer-band{position:absolute;left:26px;top:1137px;width:622px;height:19px;
    background:linear-gradient(90deg,var(--gold-dark),var(--gold-light) 50%,var(--gold-dark))}
  .notes{position:absolute;left:52px;top:142px;width:480px;list-style:none;color:var(--text);
    font-size:11.3px;line-height:16px;letter-spacing:-.1px}
  .notes li{position:relative;padding-left:12px;margin-bottom:8px}
  .notes li::before{content:"";position:absolute;left:0;top:4px;width:7px;height:7px;background:var(--paper)}
  .brand{position:absolute;left:514px;top:140px;width:104px;text-align:center;color:var(--paper)}
  .brand-mark{display:block;width:30px;height:30px;margin:0 auto 10px;border:2px solid var(--paper);border-radius:50%}
  .brand-name{font-family:"Bebas Neue",sans-serif;font-size:24px;line-height:1;letter-spacing:1px}
  .service{position:absolute;left:60px;width:551px;height:50px}
  .service-title{position:absolute;left:2px;bottom:10px;font-family:"Bebas Neue",sans-serif;font-size:26px;
    line-height:1;letter-spacing:1.4px;color:var(--paper);white-space:nowrap}
  .service-rule{position:absolute;left:4px;right:135px;bottom:0;height:1.5px;background:var(--rule)}
  .price{position:absolute;right:0;top:0;width:135px;height:50px;
    background:linear-gradient(90deg,var(--gold-mid),var(--gold-dark));
    border-bottom:1.5px solid var(--rule);
    display:flex;align-items:flex-end;padding:0 0 5px 20px;
    font-family:"Bebas Neue",sans-serif;color:var(--ink);line-height:1}
  .price-amount{font-size:42px}
  .price-note{font-size:13px;margin:0 0 3px 1px}
  .price-pre{font-size:13px;margin:0 2px 3px 0}
  .price-stack{font-size:12px;line-height:12px;margin:0 0 4px 2px}
  .price.centered{padding-left:12px}
  .desc{position:absolute;left:64px;width:572px;color:var(--text);font-size:12.8px;line-height:18px}
  .desc.justified{text-align:justify;width:548px}
</style>
</head>
<body>
<main class="menu">
  <div class="board"></div>
  <div class="board-texture" role="img" aria-label="Faint ghosted honeycomb texture across the dark background"></div>

  <header class="header-band"><h1>Interior Detail Packages</h1></header>

  <ul class="notes">
    <li>As a reminder, we would appreciate all personal items be removed from interior</li>
    <li>There may be instances were stains and pet hair are not fully removed, please understand we will do our best to remove as much as possible</li>
    <li>Please see terms and conditions (insert terms and conditions link)</li>
  </ul>

  <div class="brand">
    <span class="brand-mark"></span>
    <span class="brand-name">Crucible Garage</span>
  </div>

  <section class="service" style="top:259px">
    <h2 class="service-title">Basic Interior Clean</h2><div class="service-rule"></div>
    <div class="price"><span class="price-amount">100$</span><span class="price-note">And Up</span></div>
  </section>
  <p class="desc" style="top:316px">Full vacuum of carpet, seats, upholstery, Floormats extracted and steam cleaned, dash/doors wiped and dressed, interior glass surfaces cleaned, center console steam cleaned</p>

  <section class="service" style="top:383px">
    <h2 class="service-title">Deluxe Interior Clean</h2><div class="service-rule"></div>
    <div class="price"><span class="price-amount">$200</span><span class="price-note">And Up</span></div>
  </section>
  <p class="desc justified" style="top:443px">Basic interior package + Full steam clean and shampoo of all interior carpet and seats, leather is gently steamed and scrubbed lightly, dash/doors/vents are dusted and dressed, steering wheel and controls are deep cleaned and dressed. Headliner/visors are lightly cleaned * Heavily soiled interiors that exceed a Deluxe Package will be charged extra *</p>

  <section class="service" style="top:557px">
    <h2 class="service-title">Deep Leather Cleaning &amp; Conditioning</h2><div class="service-rule"></div>
    <div class="price"><span class="price-amount">$100</span><span class="price-note">/Row</span></div>
  </section>
  <p class="desc" style="top:618px;left:62px">Deluxe interior package + premium leather conditioning treatment</p>

  <section class="service" style="top:666px">
    <h2 class="service-title">Biohazard Cleaning</h2><div class="service-rule"></div>
    <div class="price"><span class="price-amount">$350</span></div>
  </section>
  <p class="desc" style="top:726px;left:62px">Plus Deluxe Interior Package</p>

  <section class="service" style="top:764px">
    <h2 class="service-title">Fabric Guard</h2><div class="service-rule"></div>
    <div class="price"><span class="price-amount">$100</span><span class="price-note">/Row</span></div>
  </section>
  <p class="desc" style="top:824px;left:62px">Carpet and Fabric upholstery sprayed for stain and waterproofing</p>

  <section class="service" style="top:876px">
    <h2 class="service-title">Ozone Treatment for Odors</h2><div class="service-rule"></div>
    <div class="price centered"><span class="price-pre">Add</span><span class="price-amount">$50</span><span class="price-stack">To Any<br>Pakage</span></div>
  </section>
  <p class="desc" style="top:938px;left:62px">Plus Deluxe Interior Package</p>

  <section class="service" style="top:970px">
    <h2 class="service-title">Excessive Pet Hair Removal</h2><div class="service-rule"></div>
    <div class="price centered"><span class="price-amount">10%</span><span class="price-stack">Surcharge<br>Of Total</span></div>
  </section>

  <section class="service" style="top:1051px">
    <h2 class="service-title">Trunk Area Detail</h2><div class="service-rule"></div>
    <div class="price"><span class="price-amount">$50</span><span class="price-note">And Up</span></div>
  </section>

  <div class="footer-band"></div>
</main>
</body>
</html>
```